Specialist aerospace company requires Powerpoint template

We are a company who delivers specialist engineering and testing services. We would like an updated Powerpoint template - specifically one that will be suitable to use in the production of training materials.
We would therefore like the following included:
-Our logo
-A copyright notice
-The course name (e.g. High Voltage Basics)
-The lesson name (e.g. Safe Clearances)
We wish to convey a professional image.

```html
<!DOCTYPE html>
<html lang="en">
<head>
<meta charset="utf-8">
<title>Altivolt – Training Template</title>
<link rel="stylesheet" href="https://fonts.googleapis.com/css2?family=Fira+Sans:wght@300;600;700;800&family=Mulish:wght@400&display=swap">
<style>
  :root {
    --page: #e9e9ea;
    --white: #ffffff;
    --brand-blue: #44719b;
    --ink: #3a3d42;
    --on-blue: #e6edf4;
    --night: #15171a;
    --logo-ink: #3b4a5c;
  }
  * { margin: 0; padding: 0; box-sizing: border-box; }
  html, body { width: 1200px; height: 3819px; overflow: hidden; background: var(--page); }
  body { position: relative; font-family: "Mulish", sans-serif; color: var(--ink); }

  .slide { position: absolute; left: 104px; width: 1001px; height: 562px; background: var(--white); overflow: hidden; }
  .abs { position: absolute; }
  .photo { position: absolute; }

  .brand { position: absolute; display: flex; align-items: center; gap: 10px;
    font-family: "Fira Sans", sans-serif; font-weight: 600; font-size: 34px; letter-spacing: -0.5px; color: var(--logo-ink); }
  .brand .mark { width: 28px; height: 28px; background: currentColor; }
  .brand.light { color: var(--white); }

  .heading { font-family: "Fira Sans", sans-serif; font-weight: 700; font-size: 28px; letter-spacing: 0.5px; color: var(--white); }
  .body-copy { font-size: 12px; line-height: 18.7px; text-align: justify; color: var(--on-blue); }
  .body-copy + .body-copy { margin-top: 18px; }

  /* Title */
  .title-slide { top: 107px; }
  .title-slide .photo { inset: 0; background: linear-gradient(100deg, #3b3d40 0%, #6e7278 40%, #c9cccf 70%, #e4e6e8 100%); }
  .title-slide .accent { left: 0; top: 415px; width: 10px; height: 96px; background: var(--white); }
  .title-slide .title { left: 46px; top: 414px; color: var(--white); font-family: "Fira Sans", sans-serif; line-height: 52px; }
  .title .lead { font-weight: 300; font-size: 44px; display: block; }
  .title .strong { font-weight: 700; font-size: 44px; display: block; }

  /* About */
  .about-slide { top: 709px; }
  .about-slide .photo { left: 339px; top: 0; width: 662px; height: 562px; background: radial-gradient(ellipse at 55% 45%, #2d5a60 0%, #14282d 50%, #0a1214 100%); }
  .about-slide .panel { left: 34px; top: 130px; width: 463px; height: 347px; background: var(--brand-blue); padding: 34px 40px; }
  .about-slide .heading { margin-bottom: 16px; }

  /* Course */
  .course-slide { top: 1311px; }
  .course-slide .panel { left: 368px; top: 0; width: 633px; height: 562px; background: var(--brand-blue); }
  .course-slide .photo { left: 27px; top: 89px; width: 413px; height: 439px; background: linear-gradient(135deg, #d9dadb 0%, #b9b3ad 45%, #a6574d 80%, #c9c9c9 100%); }
  .course-slide .content { left: 474px; top: 50px; width: 463px; }
  .course-slide .heading { margin-bottom: 16px; font-size: 26px; }

  /* Lesson */
  .lesson-slide { top: 1920px; }
  .lesson-slide .panel { left: 0; top: 0; width: 587px; height: 562px; background: var(--brand-blue); }
  .lesson-slide .photo { left: 522px; top: 84px; width: 463px; height: 431px; background: linear-gradient(160deg, #4d5259 0%, #9ea3a8 40%, #dcdfe2 60%, #6b6f74 100%); }
  .lesson-slide .content { left: 27px; top: 50px; width: 463px; }
  .lesson-slide .heading { margin-bottom: 16px; font-size: 26px; }

  /* Services */
  .services-slide { top: 2532px; }
  .services-slide .band { left: 0; top: 75px; width: 1001px; height: 261px; background: var(--brand-blue); }
  .services-slide .section-title { left: 294px; top: 24px; font-family: "Fira Sans", sans-serif; font-weight: 700; font-size: 25px; letter-spacing: 1px; color: var(--brand-blue); }
  .service { position: absolute; top: 102px; width: 268px; }
  .service .photo { position: relative; width: 268px; height: 171px; }
  .service h3 { font-family: "Fira Sans", sans-serif; font-weight: 700; font-size: 15px; letter-spacing: 0.5px; color: var(--white); margin-top: 29px; }
  .service p { margin-top: 42px; font-size: 12px; line-height: 19px; text-align: justify; color: var(--ink); width: 260px; }

  /* Closing */
  .closing-slide { top: 3140px; background: var(--night); }
  .closing-slide .glow { inset: 0; background: radial-gradient(circle at 68% 42%, #2c2e32 0%, #1b1d20 45%, #111214 100%); }
  .closing-slide .brand { color: #3e4650; }
  .closing-slide .thanks { left: 341px; top: 231px; width: 322px; border-top: 3px solid var(--brand-blue); border-bottom: 3px solid var(--brand-blue);
    text-align: center; font-family: "Fira Sans", sans-serif; font-weight: 800; font-size: 54px; letter-spacing: 1px; color: var(--brand-blue); line-height: 90px; }
</style>
</head>
<body>

<section class="slide title-slide">
  <div class="photo" role="img" aria-label="Engineer with a tablet inspecting a light aircraft in a hangar"></div>
  <div class="brand light" style="left:30px;top:28px;"><span class="mark"></span>altivolt</div>
  <div class="abs accent"></div>
  <h1 class="abs title"><span class="lead">WELCOME TO</span><span class="strong">ALTIVOLT</span></h1>
</section>

<section class="slide about-slide">
  <div class="brand" style="left:34px;top:32px;"><span class="mark"></span>altivolt</div>
  <div class="photo" role="img" aria-label="Technician working on electronic circuit boards in a dim lab"></div>
  <div class="abs panel">
    <h2 class="heading">ABOUT US</h2>
    <p class="body-copy">Sed ut perspiciatis unde omnis iste natus error sit voluptatem accusantium doloremque laudantium, totam rem aperiam, eaque ipsa quae ab illo inventore veritatis et quasi architecto beatae vitae dicta sunt explicabo. Nemo enim ipsam voluptatem quia voluptas sit aspernatur aut odit aut fugit, sed quia consequuntur magni dolores eos qui ratione voluptatem sequi nesciunt. Neque porro quisquam est, qui dolorem ipsum quia dolor sit amet, consectetur, adipisci velit, sed quia non numquam eius modi tempora incidunt ut labore et dolore magnam aliquam quaerat voluptatem. Ut enim ad minima veniam, quis nostrum exercitationem ullam corporis suscipit laboriosam, nisi ut aliquid ex ea commodi consequatur? Quis autem vel eum iure reprehenderit qui in</p>
  </div>
</section>

<section class="slide course-slide">
  <div class="abs panel"></div>
  <div class="brand" style="left:34px;top:22px;"><span class="mark"></span>altivolt</div>
  <div class="photo" role="img" aria-label="Hands testing a circuit with multimeter probes"></div>
  <div class="abs content">
    <h2 class="heading">HIGH VOLTAGE BASICS</h2>
    <p class="body-copy">Sed ut perspiciatis unde omnis iste natus error sit voluptatem accusantium doloremque laudantium, totam rem aperiam, eaque ipsa quae ab illo inventore veritatis et quasi architecto beatae vitae dicta sunt explicabo. Nemo enim ipsam voluptatem quia voluptas sit aspernatur aut odit aut fugit, sed quia consequuntur magni dolores eos qui ratione voluptatem sequi nesciunt. Neque porro quisquam est, qui dolorem ipsum quia dolor sit amet, consectetur, adipisci velit, sed quia non numquam eius modi tempora incidunt ut labore et dolore magnam aliquam quaerat voluptatem. Ut enim ad minima veniam, quis nostrum exercitationem ullam corporis suscipit laboriosam, nisi ut aliquid ex ea commodi consequatur? Quis autem vel eum iure reprehenderit qui in</p>
    <p class="body-copy">Sed ut perspiciatis unde omnis iste natus error sit voluptatem accusantium doloremque laudantium, totam rem aperiam, eaque ipsa quae ab illo inventore veritatis et quasi architecto beatae vitae dicta sunt explicabo. Nemo enim ipsam voluptatem quia voluptas sit aspernatur aut odit aut fugit, sed quia consequuntur magni dolores eos qui ratione voluptatem sequi nesciunt. Neque porro quisquam est, qui dolorem ipsum quia dolor sit amet, consectetur, adipisci velit, sed quia non numquam eius modi tempora incidunt ut labore et dolore magnam aliquam quaerat voluptatem. Ut enim ad minima veniam, quis nostrum exercitationem ullam corporis suscipit laboriosam, nisi ut aliquid ex ea commodi consequatur? Quis autem vel eum iure reprehenderit qui in</p>
  </div>
</section>

<section class="slide lesson-slide">
  <div class="abs panel"></div>
  <div class="brand" style="left:735px;top:18px;"><span class="mark"></span>altivolt</div>
  <div class="photo" role="img" aria-label="Rocket stage lying in an assembly hall"></div>
  <div class="abs content">
    <h2 class="heading">SAFE CLEARANCES</h2>
    <p class="body-copy">Sed ut perspiciatis unde omnis iste natus error sit voluptatem accusantium doloremque laudantium, totam rem aperiam, eaque ipsa quae ab illo inventore veritatis et quasi architecto beatae vitae dicta sunt explicabo. Nemo enim ipsam voluptatem quia voluptas sit aspernatur aut odit aut fugit, sed quia consequuntur magni dolores eos qui ratione voluptatem sequi nesciunt. Neque porro quisquam est, qui dolorem ipsum quia dolor sit amet, consectetur, adipisci velit, sed quia non numquam eius modi tempora incidunt ut labore et dolore magnam aliquam quaerat voluptatem. Ut enim ad minima veniam, quis nostrum exercitationem ullam corporis suscipit laboriosam, nisi ut aliquid ex ea commodi consequatur? Quis autem vel eum iure reprehenderit qui in</p>
    <p class="body-copy">Sed ut perspiciatis unde omnis iste natus error sit voluptatem accusantium doloremque laudantium, totam rem aperiam, eaque ipsa quae ab illo inventore veritatis et quasi architecto beatae vitae dicta sunt explicabo. Nemo enim ipsam voluptatem quia voluptas sit aspernatur aut odit aut fugit, sed quia consequuntur magni dolores eos qui ratione voluptatem sequi nesciunt. Neque porro quisquam est, qui dolorem ipsum quia dolor sit amet, consectetur, adipisci velit, sed quia non numquam eius modi tempora incidunt ut labore et dolore magnam aliquam quaerat voluptatem. Ut enim ad minima veniam, quis nostrum exercitationem ullam corporis suscipit laboriosam, nisi ut aliquid ex ea commodi consequatur? Quis autem vel eum iure reprehenderit qui in</p>
  </div>
</section>

<section class="slide services-slide">
  <div class="brand" style="left:28px;top:18px;"><span class="mark"></span>altivolt</div>
  <h2 class="abs section-title">SERVICES</h2>
  <div class="abs band"></div>
  <article class="service" style="left:37px;">
    <div class="photo" role="img" aria-label="Aircraft cockpit instrument panel" style="background:linear-gradient(160deg,#2a2c2f,#6c7076 55%,#303236);"></div>
    <h3>HEADING 1</h3>
    <p>Sed ut perspiciatis unde omnis iste natus error sit voluptatem accusantium doloremque laudantium, totam rem aperiam, eaque ipsa quae ab illo inventore veritatis et quasi architecto beatae vitae dicta sunt explicabo. Nemo enim ipsam voluptatem quia voluptas sit aspernatur aut odit aut fugit, sed quia consequuntur magni dolores eos qui ratione voluptatem sequi nesciunt.</p>
  </article>
  <article class="service" style="left:363px;">
    <div class="photo" role="img" aria-label="Precision gear machining on a lathe" style="background:linear-gradient(160deg,#3a3c40,#a7abb0 50%,#55585c);"></div>
    <h3>HEADING 2</h3>
    <p>Sed ut perspiciatis unde omnis iste natus error sit voluptatem accusantium doloremque laudantium, totam rem aperiam, eaque ipsa quae ab illo inventore veritatis et quasi architecto beatae vitae dicta sunt explicabo. Nemo enim ipsam voluptatem quia voluptas sit aspernatur aut odit aut fugit, sed quia consequuntur magni dolores eos qui ratione voluptatem sequi nesciunt.</p>
  </article>
  <article class="service" style="left:706px;">
    <div class="photo" role="img" aria-label="Mechanic servicing a jet engine on a stand" style="background:linear-gradient(160deg,#c9ccd0,#8d939a 50%,#d8dadd);"></div>
    <h3>HEADING 3</h3>
    <p>Sed ut perspiciatis unde omnis iste natus error sit voluptatem accusantium doloremque laudantium, totam rem aperiam, eaque ipsa quae ab illo inventore veritatis et quasi architecto beatae vitae dicta sunt explicabo. Nemo enim ipsam voluptatem quia voluptas sit aspernatur aut odit aut fugit, sed quia consequuntur magni dolores eos qui ratione voluptatem sequi nesciunt.</p>
  </article>
</section>

<section class="slide closing-slide">
  <div class="photo glow" role="img" aria-label="Dark close-up of a jet engine fan"></div>
  <div class="brand" style="left:52px;top:44px;"><span class="mark"></span>altivolt</div>
  <div class="abs thanks">THANK YOU</div>
</section>

</body>
</html>
```